Brindle Lawyers Banner

I would like to have a graphic design created for a company banner. The company is Brindle Lawyers and the website is https://brindlelawyers.example.au/ We would like a professional banner we are able to put up at events to advertise the company.
The banner size is 800mm wide by 2000mm high so please keep the design inside these constraints.

```html
<!DOCTYPE html>
<html lang="en">
<head>
<meta charset="utf-8">
<title>Brindle Lawyers – Event Banner</title>
<link rel="stylesheet" href="https://fonts.googleapis.com/css2?family=Montserrat:wght@300;400;700&display=swap">
<style>
  :root {
    --page-bg: #e6e6e6;
    --banner-navy: #232f42;
    --panel-slate: #2e3f58;
    --panel-teal: #24445e;
    --accent-blue: #2a9fd6;
    --text-white: #ffffff;
  }
  html, body {
    margin: 0;
    padding: 0;
    width: 1199px;
    height: 1200px;
    overflow: hidden;
    background: var(--page-bg);
  }
  .canvas {
    position: relative;
    width: 1199px;
    height: 1200px;
  }
  .banner {
    position: absolute;
    left: 371px;
    top: 30px;
    width: 456px;
    height: 1140px;
    box-shadow: 0 6px 20px rgba(0,0,0,0.18);
  }
  .banner svg { display: block; }
  .wordmark-name {
    font-family: 'Montserrat', sans-serif;
    font-weight: 400;
    fill: var(--text-white);
  }
  .wordmark-descriptor {
    font-family: 'Montserrat', sans-serif;
    font-weight: 300;
    fill: var(--text-white);
  }
  .intro-copy {
    position: absolute;
    left: 269px;
    top: 720px;
    margin: 0;
    font-family: 'Montserrat', sans-serif;
    font-weight: 700;
    font-size: 17px;
    line-height: 26.5px;
    color: var(--accent-blue);
    text-transform: uppercase;
  }
</style>
</head>
<body>
<div class="canvas">
  <div class="banner">
    <svg width="456" height="1140" viewBox="0 0 456 1140" aria-label="Brindle Lawyers banner">
      <rect class="banner-bg" width="456" height="1140" fill="var(--banner-navy)"/>
      <!-- translucent background bands -->
      <g class="background-bands" opacity="0.55">
        <rect x="79" y="0" width="100" height="1110" fill="var(--panel-slate)"/>
        <rect x="144" y="145" width="312" height="72" fill="var(--panel-teal)"/>
        <rect x="240" y="0" width="216" height="400" fill="var(--panel-slate)" opacity="0.6"/>
        <rect x="400" y="0" width="56" height="1110" fill="var(--panel-slate)"/>
        <rect x="130" y="620" width="326" height="70" fill="var(--panel-teal)"/>
        <rect x="135" y="830" width="60" height="280" fill="var(--panel-teal)"/>
        <rect x="0" y="920" width="456" height="40" fill="var(--panel-teal)" opacity="0.5"/>
      </g>
      <!-- bottom accent strip -->
      <rect class="accent-strip" x="0" y="1106" width="456" height="34" fill="var(--accent-blue)"/>
      <!-- vertical wordmark -->
      <text class="wordmark-name" transform="translate(239 1045) rotate(-90)"
            font-size="250" textLength="953" lengthAdjust="spacingAndGlyphs">BRINDLE</text>
      <text class="wordmark-descriptor" transform="translate(333 537) rotate(-90)"
            font-size="78" textLength="441" lengthAdjust="spacingAndGlyphs">LAWYERS</text>
    </svg>
    <p class="intro-copy">Brindle<br>Lawyers is a<br>leading<br>commercial<br>law firm<br>located in<br>Kestrel Vale,<br>Queensland.</p>
  </div>
</div>
</body>
</html>
```